Pale Lantern Double Sided Flyer Design

We need a double sided flyer (1/3 of an A4 which is 99mm x 210mm) developed for our Newcastle(NSW) tour. This flyer will be placed in tourist information centres and hotels. We want it to direct people to our website or be able to make bookings over the phone.

About Us:-
We are a city walking tour company that runs tours day or night. We run both day and night and will incorporate real history / real Pale lantern. Some of the stories will be quite serious i.e.- there are infamous murders from 100 years ago, baffling court cases, even a bit of poetry written by murderers, suicides, love triangles, you name it. We will be telling the historical stories that tourists will not hear from any other tour provider. A bit of darkness, a bit of mystery and a bit of history theme.

We do no go for scares and let the very real stories deliver the entertainment for our guests. Our customers enjoy our tours, but it isn't light fun and frivolity. Our stories are being carefully crafted and are packed with unexpected twists, turns; revelations whilst remaining all 100% true. We deliver deep, rich, engaging stories.

Here are a few samples of quotes from the characters in our stories that may give you an idea of the kind of history we will cover:-

"There were bits of spines, bits of skulls, [and] finger bones spilled out all over the streets - I ended up filling three boxes. Children were playing with them for weeks”

"I had a close shave last night and now I want a close haircut.”

“She's a beautiful child', isn't she? She's the cause of all the trouble.”

“I did it because she would not come home with me.”

"I have killed my wife. I’m glad she’s dead.”

"Stand aside or I'll put a bullet through both of you."

“You villain, I'll teach you to take away my character."

“You’re not dead yet, you bastard!”

Our website, booking form and contact details can be viewed at www.palelantern.com.au

Target Market(s)

Tourists

Industry/Entity Type

Tour

Colors

Designer to choose colors to be used in the design.

Requirements
Must have
• Vertical orientation please.
• Please also include a reference to a discount offer of 25% using the promo code "WICK".
Nice to have
• FRONT FLYER INFORMATION
• - Pale Lantern Logo
• - "I have killed my wife; I'm glad she's dead."
• - Harbourside Hidden Lanes Walk
• - 25% Discount Offer Codeword WICK
• - web address at the base; www.palelantern.com.au
• BACK FLYER INFORMATION
• - "She's a beautiful child', isn't she? She's the cause of all the trouble.
• - Pale Lantern Logo at the base along with the web address www.palelantern.com.au
• - Blurb:- Pale lantern brings back Newcastle's hidden past, the forgotten past, the dark past that may not want to be remembered.
• Real stories from the streets around you. Discover the histories you won't hear anywhere else. The forgotten stories of yesteryear finally get a chance to be told. Through you they get to live again.
Should not have
• GENERAL
• Please do not include the phone number, email address or social media icons. We want to drive online bookings.

```html
<!DOCTYPE html>
<html lang="en">
<head>
<meta charset="utf-8">
<title>Pale Lantern – Double Sided Flyer</title>
<link rel="stylesheet" href="https://fonts.googleapis.com/css2?family=Lato:wght@400;700&display=swap">
<style>
  :root {
    --backdrop: #a7a8ab;
    --ink-dark: #1e1e1f;
    --ink-mid: #2b2b2c;
    --accent-red: #e3262d;
    --paper-white: #ffffff;
    --pill-text: #333333;
  }
  * { margin: 0; padding: 0; box-sizing: border-box; }
  html, body {
    width: 1200px; height: 1193px; overflow: hidden;
    background: var(--backdrop);
    font-family: "Lato", sans-serif;
    color: var(--paper-white);
  }
  .flyer {
    position: absolute; top: 84px;
    width: 479px; height: 1016px;
    overflow: hidden;
    background: var(--ink-dark);
    box-shadow: 6px 8px 14px rgba(0,0,0,0.35);
  }
  .flyer--front { left: 93px; }
  .flyer--back { left: 622px; }

  .flyer__photo { position: absolute; left: 0; top: 0; width: 100%; }
  .flyer--front .flyer__photo {
    height: 640px;
    background: linear-gradient(180deg, #4c5561 0%, #6b6f74 22%, #9a8e74 38%, #c3a466 44%, #6c6a55 50%, #5b5c58 56%, #8b8a80 66%, #6a6d72 80%, #505459 100%);
  }
  .flyer--back .flyer__photo {
    height: 500px;
    background: linear-gradient(170deg, #1b1b1b 0%, #3d3d3d 30%, #5a5a5a 50%, #2e2e2e 75%, #444 100%);
  }
  .flyer__panel { position: absolute; left: 0; top: 0; }

  .brand-name {
    position: absolute; left: 0; width: 100%;
    text-align: center; font-weight: 700;
    font-size: 31px; letter-spacing: 0.5px;
    color: var(--paper-white);
  }
  .tour-title {
    position: absolute; left: 0; width: 100%; top: 203px;
    text-align: center; font-size: 16px; text-transform: uppercase;
  }
  .front-quote {
    position: absolute; top: 414px; left: 62px; width: 356px;
    font-weight: 700; font-size: 28px; line-height: 31px;
    text-shadow: 0 1px 4px rgba(0,0,0,0.5);
  }
  .front-quote span { display: block; }
  .front-quote .line-two { text-align: right; }

  .front-blurb {
    position: absolute; top: 604px; left: 56px; width: 368px;
    text-align: center; font-size: 15.2px; line-height: 20.5px;
  }
  .offer { position: absolute; top: 800px; left: 75px; display: flex; align-items: center; }
  .offer__percent { color: var(--accent-red); font-size: 74px; line-height: 1; letter-spacing: -2px; }
  .offer__label { margin-left: 16px; font-size: 33px; line-height: 31px; text-transform: uppercase; }
  .codeword {
    position: absolute; top: 886px; left: 75px; width: 329px; height: 47px;
    display: flex; border-radius: 24px; overflow: hidden;
  }
  .codeword__label {
    width: 165px; background: var(--paper-white); color: var(--pill-text);
    font-size: 25px; display: flex; align-items: center; justify-content: center;
  }
  .codeword__code {
    flex: 1; background: var(--accent-red); border-radius: 24px;
    font-size: 33px; display: flex; align-items: center; justify-content: center;
  }

  .back-quote {
    position: absolute; top: 160px; left: 20px; width: 439px;
    text-align: center; font-weight: 700; font-size: 28px; line-height: 36px;
    text-shadow: 0 1px 4px rgba(0,0,0,0.6);
  }
  .about-heading {
    position: absolute; top: 448px; left: 0; width: 100%;
    text-align: center; color: var(--accent-red); font-weight: 700; font-size: 28px;
  }
  .about-body {
    position: absolute; top: 506px; left: 50px; width: 379px;
    text-align: center; font-size: 18.5px; line-height: 24.6px;
  }
  .about-body p + p { margin-top: 24.6px; }

  .web-band {
    position: absolute; left: 0; bottom: 0; width: 100%; height: 51px;
    background: var(--accent-red);
    display: flex; align-items: center; justify-content: center;
    font-size: 31px;
  }
</style>
</head>
<body>

<section class="flyer flyer--front">
  <div class="flyer__photo" role="img" aria-label="Photo of a city skyline at dusk reflected in a river"></div>
  <svg class="flyer__panel" width="479" height="1016" viewBox="0 0 479 1016" aria-hidden="true">
    <path d="M0,613 Q239.5,423 479,613 L479,1016 L0,1016 Z" fill="var(--ink-dark)"/>
    <path d="M0,613 Q239.5,423 479,613" fill="none" stroke="var(--accent-red)" stroke-width="2.5"/>
  </svg>
  <div class="brand-name" style="top:128px;">PALE LANTERN</div>
  <div class="tour-title">Harbourside Hidden Lanes Walk</div>
  <blockquote class="front-quote">
    <span class="line-one">"I have killed my wife;</span>
    <span class="line-two">I'm glad she's dead."</span>
  </blockquote>
  <p class="front-blurb">Dark; a euphemism for the unknown or the forgotten.....the dark ages, dark matter, dark energy; things where knowledge is uncertain or unknown are dark.&nbsp; Pale lantern brings back the hidden past, the forgotten past, the past that may not want to be remembered......but these are real stories....real stories that come from the streets around you.</p>
  <div class="offer">
    <span class="offer__percent">25%</span>
    <span class="offer__label">Discount<br>Offer</span>
  </div>
  <div class="codeword">
    <span class="codeword__label">Codeword</span>
    <span class="codeword__code">WICK</span>
  </div>
  <div class="web-band">www.palelantern.com.au</div>
</section>

<section class="flyer flyer--back">
  <div class="flyer__photo" role="img" aria-label="Black and white aerial photo of a coastal city with buildings and ocean"></div>
  <svg class="flyer__panel" width="479" height="1016" viewBox="0 0 479 1016" aria-hidden="true">
    <path d="M0,482 Q239.5,282 479,482 L479,1016 L0,1016 Z" fill="var(--ink-dark)"/>
    <path d="M0,482 Q239.5,282 479,482" fill="none" stroke="var(--accent-red)" stroke-width="2.5"/>
  </svg>
  <blockquote class="back-quote">She's a beautiful child', isn't she? She's the cause of all the trouble.</blockquote>
  <h2 class="about-heading">About Us</h2>
  <div class="about-body">
    <p>Pale lantern brings back Newcastle's hidden past, the forgotten past, the dark past that may not want to be remem-bered.</p>
    <p>- Real stories from the streets around you. Discover the histories you won't hear anywhere else. The forgotten stories of yesteryear finally get a chance to be told. Through you they get to live again.</p>
  </div>
  <div class="brand-name" style="top:868px;">PALE LANTERN</div>
  <div class="web-band">www.palelantern.com.au</div>
</section>

</body>
</html>
```